Web Site Design

We need to design the whole web site for our small start up. We sell hospitality and culinary art internships abroad. I did my own design with WIX which is horrible meanwhile I started with my business. You can see it www.brightvoyage-intern.example I will need you to create a new and attractive web site and to leave it working on wix. The internship destinations are United Arab Emirates, Thailand, China, Spain, Brazil and maybe leave a couple of pages for future destinations.You could also get other ideas of other sites that do internships.

Target Market(s)

Students and recent graduates of hospitality and culinary art majors

Industry/Entity Type

Education

Number of Pages Required

5+ page

Requirements
Must have
• Addittional to our program destinations, or to the pages in the current site. The website must contain a page for Universities or Hotels who require our service

```html
<!DOCTYPE html>
<html lang="en">
<head>
<meta charset="utf-8">
<title>Bright Voyage — Hospitality Internships Abroad</title>
<link href="https://fonts.googleapis.com/css2?family=Noticia+Text:wght@400;700&family=Questrial&display=swap" rel="stylesheet">
<style>
:root{
  --teal:#2b8284;
  --teal-dark:#1f6e70;
  --teal-title:#237c80;
  --ink:#1b1b1b;
  --text:#444;
  --mist:#e3f7f9;
  --footer:#1f1f1f;
  --footer-line:#333;
  --footer-text:#9a9a9a;
  --white:#fff;
}
*{box-sizing:border-box;margin:0;padding:0}
html,body{width:1200px;height:2449px;overflow:hidden}
body{position:relative;background:var(--white);font-family:"Questrial",sans-serif;color:var(--text)}
.abs{position:absolute}

/* header */
.site-header{left:0;top:0;width:1200px;height:67px;background:var(--white);box-shadow:0 2px 6px rgba(0,0,0,.08);z-index:3}
.brand{display:flex;align-items:center;gap:10px}
.brand-mark{width:40px;height:40px;border-radius:50%;border:2px solid #b9c7c7}
.brand-name{font-family:"Questrial",sans-serif;font-size:24px;color:var(--teal)}
.site-header .brand{left:163px;top:13px}
.main-nav{left:485px;top:24px;display:flex;font-size:12px;color:var(--ink)}
.main-nav span{margin-right:18px}
.main-nav .sep{color:#666}
.social{display:flex;gap:4px}
.social i{display:block;width:22px;height:22px;border-radius:50%;background:var(--teal)}
.site-header .social{left:916px;top:22px}

/* hero */
.hero{left:0;top:67px;width:1200px;height:562px;background:linear-gradient(100deg,#3f8f8a 0%,#5aa6a3 30%,#6db2b0 55%,#4f9d9d 80%,#3c8d8e 100%)}
.welcome-card{left:219px;top:245px;width:762px;height:392px;background:var(--white)}
.welcome-title{left:0;top:42px;width:762px;text-align:center;font-family:"Noticia Text",serif;font-weight:700;font-size:27px;color:var(--teal-title);letter-spacing:.5px}
.campus-photo{left:23px;top:109px;width:446px;height:283px;background:linear-gradient(180deg,#6fa6dc 0%,#a9c9e8 30%,#b85c45 45%,#8a7d6a 65%,#5f8a6a 80%,#8fa8b8 100%)}
.program{left:509px;top:142px;width:240px}
.program h2{font-family:"Noticia Text",serif;font-weight:700;font-size:24px;line-height:34px;color:var(--ink)}
.program p{margin-top:14px;font-size:13px;line-height:22px;color:#666}
.btn-outline{display:inline-block;margin-top:18px;border:2px solid var(--teal);padding:9px 16px;font-size:12px;font-weight:700;color:var(--teal)}

/* enquiry */
.enquiry{left:162px;top:660px;width:877px;height:426px;background:linear-gradient(160deg,#d9f4f7 0%,var(--mist) 40%,#effbfc 60%,#d7f1f4 100%)}
.enquiry h3{left:0;top:52px;width:877px;text-align:center;font-family:"Noticia Text",serif;font-weight:400;font-size:25px;line-height:37px;color:var(--ink)}
.field{background:var(--white);font-size:11px;color:#999;padding:12px 14px}
.f-name{left:91px;top:196px;width:343px;height:39px}
.f-email{left:442px;top:196px;width:343px;height:39px}
.f-message{left:91px;top:243px;width:343px;height:87px}
.f-subject{left:442px;top:243px;width:343px;height:41px}
.btn-submit{left:442px;top:290px;width:343px;height:40px;background:var(--teal);color:var(--white);font-size:12px;font-weight:700;text-align:center;line-height:40px;letter-spacing:.5px}
.tagline{left:0;top:357px;width:877px;text-align:center;font-size:12px;font-weight:700;letter-spacing:1.5px;color:var(--ink)}

/* destinations */
.destinations{left:162px;top:1086px;width:877px;height:825px;display:grid;grid-template-columns:1fr 1fr}
.dest{position:relative;height:412.5px;text-align:center;color:var(--white)}
.dest-china{background:linear-gradient(180deg,#2a3548 0%,#3c4560 40%,#5a3c52 65%,#3a2a2a 100%)}
.dest-spain{background:linear-gradient(180deg,#0d1a2e 0%,#1c2a40 45%,#4a3a2c 75%,#2a1e18 100%)}
.dest-australia{background:linear-gradient(180deg,#3c4a5c 0%,#5b6675 35%,#2e3a4a 65%,#3a2e22 100%)}
.dest-france{background:linear-gradient(180deg,#1c3a6a 0%,#2f4f80 45%,#2c4a5a 75%,#1e3040 100%)}
.dest h4{margin-top:100px;font-family:"Noticia Text",serif;font-weight:700;font-size:25px;text-decoration:underline;text-underline-offset:4px}
.dest p{width:290px;margin:22px auto 0;font-size:12px;line-height:22px}
.btn-fill{display:inline-block;margin-top:24px;width:97px;height:38px;line-height:38px;background:var(--teal);font-size:11px;font-weight:700}

/* subscribe */
.subscribe-title{left:176px;top:1977px;font-family:"Noticia Text",serif;font-weight:700;font-size:25px;color:var(--ink)}
.subscribe-form{left:575px;top:1969px;width:449px;height:51px;border:2px solid var(--teal);padding:5px}
.subscribe-input{left:6px;top:6px;width:337px;height:36px;background:#ececec;display:flex;align-items:center;gap:10px;padding-left:18px;font-size:11px;color:#555}
.btn-send{left:344px;top:6px;width:94px;height:36px;background:var(--teal);color:var(--white);text-align:center;line-height:36px;font-size:12px;font-weight:700}

/* footer */
.site-footer{left:0;top:2079px;width:1200px;height:370px;background:var(--footer);color:var(--footer-text);font-size:11px}
.site-footer .brand{left:162px;top:78px}
.site-footer .brand-mark{border-color:#8a9898}
.footer-heading{font-size:11px;font-weight:700;color:var(--white);letter-spacing:.5px}
.footer-heading::after{content:"";display:block;width:40px;height:1px;background:#666;margin-top:9px}
.company{left:162px;top:145px;width:250px}
.address{margin-top:14px;display:flex;align-items:center;gap:8px}
.company p{margin-top:10px;line-height:18px}
.info{left:545px;top:73px}
.quick{left:926px;top:73px}
.link-list{list-style:none;line-height:24px;margin-top:18px}
.info-col2{left:754px;top:119px}
.footer-rule{left:0;top:273px;width:1200px;height:1px;background:var(--footer-line)}
.copyright{left:162px;top:306px;line-height:18px}
.contact{left:506px;top:299px;font-size:12px;line-height:24px;text-align:center}
.contact .country{color:var(--teal);margin-right:8px;letter-spacing:.5px}
.site-footer .social{left:914px;top:311px}
</style>
</head>
<body>

<header class="site-header abs">
  <div class="brand abs"><span class="brand-mark"></span><span class="brand-name">Bright Voyage</span></div>
  <nav class="main-nav abs">
    <span>Home</span><span class="sep">/</span><span>Destinations</span><span class="sep">/</span><span>Universities</span><span class="sep">/</span><span>Hotels</span><span class="sep">/</span><span>Contact Us</span>
  </nav>
  <div class="social abs"><i></i><i></i><i></i><i></i><i></i></div>
</header>

<section class="hero abs" role="img" aria-label="Smiling students walking across a leafy campus, under a teal tint"></section>

<section class="welcome-card abs">
  <h1 class="welcome-title abs">WELCOME TO THE BRIGHT VOYAGE</h1>
  <div class="campus-photo abs" role="img" aria-label="Modern brick campus building behind a long reflecting pool"></div>
  <div class="program abs">
    <h2>Hospitality Internship Program</h2>
    <p>// Culinary - F&amp;B - Front Office - Guest Relations</p>
    <span class="btn-outline">Contact US</span>
  </div>
</section>

<section class="enquiry abs">
  <h3 class="abs">Hospitality Internships are Our Specialty! Take<br>Your Paid internship in One of Our Top<br>International Five-Star Hotels</h3>
  <div class="field f-name abs">Name</div>
  <div class="field f-email abs">E-mail</div>
  <div class="field f-message abs">Message</div>
  <div class="field f-subject abs">Subject</div>
  <div class="btn-submit abs">SUBMIT</div>
  <p class="tagline abs">MAKE YOUR RESUME STAND OUT WITH AN INTERNATIONAL EXPERIENCE</p>
</section>

<section class="destinations abs">
  <article class="dest dest-china" role="img" aria-label="China city skyline and pagoda at night">
    <h4>China</h4>
    <p>Chinese tourists are flocking abroad. With higher earning power, more Chinese people are visiting places such as the UK, USA, Australia and Latin America for tourism.</p>
    <span class="btn-fill">Learn More</span>
  </article>
  <article class="dest dest-spain" role="img" aria-label="Domed Madrid building and street lights at night">
    <h4>Spain</h4>
    <p>Every year millions of tourists travel to Spain, the country has been one of the most important tourist destinations of the last decadesbecom-ing the third most popular travel.</p>
    <span class="btn-fill">Learn More</span>
  </article>
  <article class="dest dest-australia" role="img" aria-label="Sydney harbour with opera house and bridge at dusk">
    <h4>Australia</h4>
    <p>Moving to Australia means running towards opportunities: Australia is a new country where the population, the economy, and the opportu-nities are growing quickly.</p>
    <span class="btn-fill">Learn More</span>
  </article>
  <article class="dest dest-france" role="img" aria-label="Paris tower beside the river under a blue sky">
    <h4>Francia</h4>
    <p>Famous for its wines and cheeses, France is the world's most popular tourist destination receiv-ing 82 million foreign tourists annual. If you are majoring in hospitality, tourism or culinary</p>
    <span class="btn-fill">Learn More</span>
  </article>
</section>

<h3 class="subscribe-title abs">Subscribe to Our Mailing List</h3>
<div class="subscribe-form abs">
  <div class="subscribe-input abs">
    <svg width="14" height="11" viewBox="0 0 14 11"><rect x="0.5" y="0.5" width="13" height="10" fill="none" stroke="#666"/><path d="M0.5 0.5 L7 6 L13.5 0.5" fill="none" stroke="#666"/></svg>
    Enter Your E-mail
  </div>
  <div class="btn-send abs">SEND</div>
</div>

<footer class="site-footer abs">
  <div class="brand abs"><span class="brand-mark"></span><span class="brand-name">Bright Voyage</span></div>
  <div class="company abs">
    <h5 class="footer-heading">COMPANY INFO</h5>
    <div class="address">
      <svg width="18" height="14" viewBox="0 0 18 14"><path d="M1 7 L9 1 L17 7" fill="none" stroke="#bbb" stroke-width="1.6"/><path d="M4 6 V13 H14 V6" fill="#bbb"/></svg>
      <span>ADDRESS :</span>
    </div>
    <p>Lorem ipsum is dummy text printing industry<br>&amp; typsetting industrytext..</p>
  </div>
  <div class="info abs">
    <h5 class="footer-heading">INFORMATION</h5>
    <ul class="link-list"><li>Home</li><li>Destinations</li><li>Universities</li><li>Hotels</li><li>Contact US</li></ul>
  </div>
  <ul class="link-list info-col2 abs" style="margin-top:0"><li>Site Map</li><li>Login</li><li>Help</li><li>Support</li></ul>
  <div class="quick abs">
    <h5 class="footer-heading">QUICK LINKS</h5>
    <ul class="link-list"><li>Privacy Policy</li><li>Terms and Condition</li></ul>
  </div>
  <div class="footer-rule abs"></div>
  <p class="copyright abs">Copyright ©2018 Bright-Voyage.<br>All Rights Reserved</p>
  <div class="contact abs">
    <div><span class="country">MEXICO</span>+52 55 0100 4321
      <svg width="12" height="12" viewBox="0 0 12 12" style="margin-left:6px;vertical-align:-1px"><path d="M2.5 0.8 L4.6 3.4 L3.4 4.8 Q4.6 7.3 7.2 8.6 L8.6 7.4 L11.2 9.5 L9.8 11.2 Q5.2 11 0.8 2.2 Z" fill="#ddd"/></svg>
    </div>
    <div>info@brightvoyage-intern.example</div>
  </div>
  <div class="social abs"><i></i><i></i><i></i><i></i><i></i></div>
</footer>

</body>
</html>
```